Business Card Design Project

We would need a business name card for our online website business, http://www.brindle.com.sg/. We would need to include our website on the name card as well.

Target Market(s)

Adults and kids in Singapore, mainly expatriates

Industry/Entity Type

Business

Font styles to use
Sans Serif

Colors

Designer to choose colors to be used in the design.

Requirements
Must have
• Must include our "vorn" logo and we would like our name card to be printed on light craft paper material

```html
<!DOCTYPE html>
<html lang="en">
<head>
<meta charset="utf-8">
<title>vorn business card</title>
<link rel="stylesheet" href="https://fonts.googleapis.com/css2?family=Roboto:wght@400;500&display=swap">
<style>
  :root {
    --backdrop: #e9e4dc;
    --brand-blue: #2f4fa2;
    --brand-blue-deep: #23408c;
    --brand-red: #d9263f;
    --ink-black: #0c0c0d;
    --paper-white: #f6f6f6;
    --text-light: #ffffff;
    --text-muted: #d8dcea;
  }
  * { margin: 0; padding: 0; box-sizing: border-box; }
  html, body {
    width: 1200px; height: 858px; overflow: hidden;
    background: var(--backdrop);
    font-family: "Roboto", Arial, sans-serif;
  }
  .canvas { position: relative; width: 1200px; height: 858px; }
  .card {
    position: absolute; width: 600px; height: 343px; left: 300px;
    overflow: hidden; border-radius: 4px;
    box-shadow: 0 10px 28px rgba(0,0,0,.22);
  }
  .card--front { top: 64px; }
  .card--back { top: 451px; }
  .card__art { position: absolute; inset: 0; width: 600px; height: 343px; }

  .brand { position: absolute; display: flex; align-items: center; gap: 10px; }
  .brand__dot { width: 26px; height: 26px; border-radius: 50%; background: var(--brand-red); }
  .brand__name { font-size: 34px; font-weight: 500; letter-spacing: 1px; }
  .card--front .brand { left: 40px; top: 156px; }
  .card--front .brand__name { color: var(--text-light); }
  .card--back .brand { left: 420px; top: 275px; }
  .card--back .brand__name { color: var(--brand-blue); }

  .holder { position: absolute; left: 40px; bottom: 38px; color: var(--text-light); }
  .holder__name { font-size: 22px; font-weight: 400; letter-spacing: .5px; }
  .holder__role { font-size: 12px; color: #cfcfcf; margin-top: 4px; }

  .contact { position: absolute; left: 388px; top: 96px; list-style: none; }
  .contact__item {
    display: flex; align-items: center; gap: 10px;
    color: var(--text-light); font-size: 15px; margin-bottom: 15px;
  }
  .contact__icon { width: 14px; height: 14px; fill: var(--text-light); flex: none; }

  .tagline {
    position: absolute; left: 40px; top: 40px; width: 420px;
    color: var(--text-light); font-size: 19px; line-height: 1.45;
  }
</style>
</head>
<body>
<main class="canvas">

  <section class="card card--front" aria-label="Card front">
    <svg class="card__art" viewBox="0 0 600 343" aria-hidden="true">
      <defs>
        <linearGradient id="blueFront" x1="0" y1="0" x2="1" y2="1">
          <stop offset="0" stop-color="#3556ad"/>
          <stop offset="1" stop-color="#26428f"/>
        </linearGradient>
        <linearGradient id="blackFront" x1="0" y1="0" x2="1" y2="1">
          <stop offset="0" stop-color="#2a2a2c"/>
          <stop offset=".5" stop-color="#0c0c0d"/>
          <stop offset="1" stop-color="#1a1a1b"/>
        </linearGradient>
      </defs>
      <rect width="600" height="343" fill="url(#blueFront)"/>
      <path d="M0 0 H338 C312 110 322 240 356 343 H0 Z" fill="var(--brand-red)" stroke="#fff" stroke-width="2"/>
      <path d="M0 0 H232 C320 80 352 220 334 343 H0 Z" fill="url(#blackFront)" stroke="#fff" stroke-width="1.5"/>
    </svg>

    <div class="brand">
      <span class="brand__dot"></span>
      <span class="brand__name">vorn</span>
    </div>

    <div class="holder">
      <p class="holder__name">EMPLOYEE NAME</p>
      <p class="holder__role">Managing Director</p>
    </div>

    <ul class="contact">
      <li class="contact__item">
        <svg class="contact__icon" viewBox="0 0 16 16"><path d="M3 1h3l1.5 4-2 1.5a9 9 0 0 0 4 4L11 8.5l4 1.5v3a2 2 0 0 1-2 2A12 12 0 0 1 1 3a2 2 0 0 1 2-2z"/></svg>
        (+65) 6400 1520
      </li>
      <li class="contact__item">
        <svg class="contact__icon" viewBox="0 0 16 16"><path d="M4 1h8v4H4z M1 6h14v7h-3v2H4v-2H1z M5 10v4h6v-4z"/></svg>
        (+65) 6400 1527
      </li>
      <li class="contact__item">
        <svg class="contact__icon" viewBox="0 0 16 16"><path d="M1 3h14v10H1z M2 4l6 5 6-5" stroke="#2f4fa2" stroke-width="1.2"/></svg>
        hello@brindlecorp.com
      </li>
      <li class="contact__item">
        <svg class="contact__icon" viewBox="0 0 16 16"><circle cx="8" cy="8" r="7"/><path d="M1 8h14 M8 1c-3 4-3 10 0 14 M8 1c3 4 3 10 0 14" stroke="#2f4fa2" stroke-width="1" fill="none"/></svg>
        www.brindle.com.sg
      </li>
    </ul>
  </section>

  <section class="card card--back" aria-label="Card back">
    <svg class="card__art" viewBox="0 0 600 343" aria-hidden="true">
      <defs>
        <linearGradient id="blueBack" x1="0" y1="0" x2="1" y2="1">
          <stop offset="0" stop-color="#3556ad"/>
          <stop offset="1" stop-color="#23408c"/>
        </linearGradient>
        <linearGradient id="whiteBack" x1="0" y1="0" x2="0" y2="1">
          <stop offset="0" stop-color="#ffffff"/>
          <stop offset="1" stop-color="#e8e8e8"/>
        </linearGradient>
      </defs>
      <rect width="600" height="343" fill="url(#whiteBack)"/>
      <path d="M0 118 C200 205 420 232 600 236 V0 H0 Z" fill="var(--brand-red)"/>
      <path d="M0 106 C210 182 420 204 600 196 V0 H0 Z" fill="url(#blueBack)" stroke="#fff" stroke-width="1.5"/>
    </svg>

    <p class="tagline">A paradise for<br>chocolates, candies, snacks &amp; drinks lovers!</p>

    <div class="brand">
      <span class="brand__dot"></span>
      <span class="brand__name">vorn</span>
    </div>
  </section>

</main>
</body>
</html>
```